Safety Work Area Signage to keep people away from work zone

We would like to create a simple design that will include our logo and phone number, 'work area', and 'caution / cuidado' (please see a mock-up of the intended design in the uploaded files). Please provide multiple options. We would like a Professional look for the poster as it is meant for safety. Poster Size to be: 18.16" X 23.10"

Target Market(s)

General Public on Construction Sites

Font styles to use
Serif

Requirements
Must have
• see mock-ups in uploaded files
Nice to have
• Simple Design, Professional Look

```html
<!DOCTYPE html>
<html lang="en">
<head>
<meta charset="utf-8">
<title>Caution Work Area Sign</title>
<link rel="stylesheet" href="https://fonts.googleapis.com/css2?family=Noto+Serif:wght@700;800&display=swap">
<style>
  :root {
    --sign-white: #ffffff;
    --hazard-red: #be1e2d;
    --band-blue: #2e3192;
    --ink-navy: #2b2b8f;
  }
  html, body {
    margin: 0;
    padding: 0;
    width: 921px;
    height: 1200px;
    overflow: hidden;
    background: var(--sign-white);
  }
  .sign {
    position: relative;
    width: 921px;
    height: 1200px;
    background: var(--sign-white);
  }
  .sign-art {
    display: block;
    width: 921px;
    height: 1200px;
    font-family: "Noto Serif", Georgia, serif;
    font-weight: 700;
  }
  .hazard-stripe { fill: var(--hazard-red); }
  .band { fill: var(--band-blue); }
  .band-text { fill: var(--sign-white); font-weight: 700; }
  .headline { fill: var(--hazard-red); font-weight: 800; }
  .company-name, .company-trade, .phone { fill: var(--ink-navy); font-weight: 700; }
  .divider { stroke: var(--ink-navy); stroke-width: 3; }
</style>
</head>
<body>
<main class="sign">
  <svg class="sign-art" viewBox="0 0 921 1200" xmlns="http://www.w3.org/2000/svg">
    <defs>
      <pattern id="hazard-pattern" width="63" height="60" patternUnits="userSpaceOnUse" patternTransform="translate(20 0) skewX(-38)">
        <rect class="hazard-stripe" x="0" y="0" width="31" height="60"/>
      </pattern>
    </defs>

    <rect class="hazard-band" x="20" y="17" width="880" height="56" fill="url(#hazard-pattern)"/>

    <g class="caution-band">
      <rect class="band" x="56" y="103" width="801" height="126"/>
      <text class="band-text" x="101" y="214" font-size="130" textLength="700" lengthAdjust="spacingAndGlyphs">CAUTION</text>
    </g>

    <text class="headline" x="62" y="456" font-size="259" textLength="840" lengthAdjust="spacingAndGlyphs">WORK</text>
    <text class="headline" x="62" y="690" font-size="290" textLength="840" lengthAdjust="spacingAndGlyphs">AREA</text>

    <g class="company">
      <text class="company-name" x="268" y="798" font-size="48" text-anchor="middle">Harlan &amp;</text>
      <text class="company-name" x="268" y="848" font-size="48" text-anchor="middle">Company, Inc.</text>
      <line class="divider" x1="458" y1="747" x2="458" y2="862"/>
      <text class="company-trade" x="660" y="798" font-size="52" text-anchor="middle">General</text>
      <text class="company-trade" x="660" y="848" font-size="52" text-anchor="middle">Contractors</text>
    </g>

    <text class="phone" x="227" y="929" font-size="66" textLength="471" lengthAdjust="spacingAndGlyphs">(407) 555-0148</text>

    <g class="cuidado-band">
      <rect class="band" x="56" y="966" width="801" height="129"/>
      <text class="band-text" x="100" y="1079" font-size="133" textLength="713" lengthAdjust="spacingAndGlyphs">CUIDADO</text>
    </g>

    <rect class="hazard-band" x="20" y="1125" width="880" height="57" fill="url(#hazard-pattern)"/>
  </svg>
</main>
</body>
</html>
```